依頼詳細
<現状の課題>
①一目で、メガネ・コンタクトの取扱いのお店とわからない。
※地域密着型(関東近郊)で隣に眼科が併設されている店舗になります。
②ターゲットにあったサイトデザインになってない。
(詳細は添付”コンセプトワーク”を参照ください)

<現在のサイト>
明確なHPの情報共有はできませんが、トップページの情報を一部伏せて共有します。
添付 ”トップページ” を参照ください。

<イメージサイト>
http://www.kumoringo.jp/
写真多めのポップデザインとして
http://www2.tanpopoko.co.jp/
コンテンツの配置やメインターゲットへの訴求の仕方
http://www.mufuta.jp/
商品、店舗(施設)の見せ方

<重視する点/検討基準>
① デザイン性(ペルソナにあったデザイン)
② 納期厳守

<具体的な制作数>
TOPページ:1ページ

<選考の進め方>
ご提案頂いたデザイン内容・コンセプトなどをもとに、プロジェクトメンバーで選考、決定致します。
※今回は、トップページのデザインのみの見積もりとなります。
今後、コーディングを依頼する可能性もございます。(別途見積もり)

以上です。
Pivoraの皆さまからの、素晴らしい提案をお待ちしております。
宜しくお願い致します。
ページ数
1ページ
希望イメージ
シンプル 複雑
単色 カラフル
暗い 明るい
日常 高級
遊び心 厳粛
未来的 伝統的
女性的 男性的
希望する色
緑系、黄・オレンジ系、コンセプトカラー(ホワイト6割、グリーン3割、オレンジ1割の配色 ※あくまで弊社のイメージです)
納品ファイル
• イラストレーター形式 (.ai)
• フォトショップ形式 (.psd)
補足説明
コンセプトカラーもこれから決めていくため、自由に提案頂きたいです。
現在はメインとなるコンセプトカラーを3色ほどで考えています。
依頼公開後の追記内容
※提案数によっては期限延長する場合がございますのでご容赦ください。
※期限6/9⇒6/11へ延長致します。
選定時期は順次報告致します。
ご提案頂いておりました皆様へ

今回、7/2選定期限となっておりましたが、
弊社での選定に時間がかかっております。

誠に申し訳ございませんが、
7/8に期間延長をさせて頂きました。

今しばらくお待ちくださいませ。
今後ともよろしくお願い致します。
■ 選んだ理由

当選:hikaru7721様
次点:tovelin様、pomme_grise様
クライアント様と協議させて頂き、総合的なバランスを評価させて頂きました。
その中で、1番クライアント様からお声が多かった「hikaru7721様」を当選とさせていただきました。ありがとうございました。

■ 提案者全員のお礼・コメント

いずれもそれぞれに良いものがあり、大いに悩んで選択させて頂きました。ご提案頂いた皆様に心より感謝申し上げます。

また、今回選定が遅れてしまったこと大変申し訳ございませんでした。

機会があれば、今後ともよろしくお願い致します。

```html
<!DOCTYPE html>
<html lang="ja">
<head>
<meta charset="utf-8">
<title>〇〇眼鏡店 トップページ</title>
<link href="https://fonts.googleapis.com/css2?family=M+PLUS+Rounded+1c:wght@400;500;700;800&display=swap" rel="stylesheet">
<style>
:root{
  --pink:#ef8a80;
  --pink-deep:#e56f66;
  --pink-pale:#fdeeea;
  --pink-soft:#f9d3cc;
  --grey-band:#ededed;
  --ink:#5a5350;
  --ink-light:#8f8784;
  --white:#ffffff;
  --blue:#7fb3e0;
  --yellow:#f2c65a;
  --green:#8fcb8a;
  --photo-a:#e9e4df;
  --photo-b:#cfd8df;
}
*{box-sizing:border-box;margin:0;padding:0}
html,body{width:1200px;height:2180px;overflow:hidden;background:var(--white)}
body{font-family:"M PLUS Rounded 1c",sans-serif;color:var(--ink)}
.page{position:relative;width:1200px;height:2180px;overflow:hidden}
.abs{position:absolute}
.photo{position:absolute;background:linear-gradient(135deg,var(--photo-a),var(--photo-b))}

/* header */
.site-header{position:absolute;left:0;top:0;width:1200px;height:124px;background:var(--white)}
.logo{position:absolute;left:240px;top:12px;font-size:34px;font-weight:800;color:var(--pink);letter-spacing:2px}
.util-tabs{position:absolute;right:250px;top:0;display:flex;gap:6px}
.util-tabs span{background:var(--pink);color:var(--white);font-size:11px;padding:6px 14px;border-radius:0 0 8px 8px}
.global-nav{position:absolute;left:240px;top:70px;width:720px;height:46px;display:flex;border-top:1px solid #f0e4e1}
.global-nav a{flex:1;display:flex;flex-direction:column;align-items:center;justify-content:center;gap:3px;font-size:10px;color:var(--ink);text-decoration:none;border-right:1px dotted #e6d6d2;white-space:nowrap}
.global-nav a svg{width:18px;height:18px}
.global-nav a.active{background:var(--pink);color:var(--white);border-radius:0 0 10px 10px}

/* hero */
.hero{position:absolute;left:0;top:128px;width:1200px;height:370px}
.hero .side{opacity:.55}
.hero-copy{position:absolute;left:300px;top:60px;color:var(--white);font-weight:800;font-size:34px;line-height:1.45;text-shadow:0 2px 6px rgba(120,90,80,.45)}
.hero-sub{position:absolute;left:300px;top:190px;font-size:13px;color:var(--white);line-height:1.7;text-shadow:0 1px 4px rgba(120,90,80,.6)}
.hero-arrow{position:absolute;top:165px;width:30px;height:40px;background:rgba(255,255,255,.75);display:flex;align-items:center;justify-content:center}
.dots{position:absolute;left:0;top:500px;width:1200px;display:flex;justify-content:center;gap:8px}
.dots i{width:8px;height:8px;border-radius:50%;background:#d8d0ce}
.dots i.on{background:var(--pink)}

/* feature band */
.feature-band{position:absolute;left:0;top:524px;width:1200px;height:404px;background:var(--grey-band)}
.card{position:absolute;background:var(--white);border-radius:8px;overflow:hidden;box-shadow:0 2px 4px rgba(0,0,0,.06)}
.card-title{background:var(--pink);color:var(--white);font-weight:700;font-size:17px;text-align:center;padding:9px 0}
.card-title.alt{background:var(--white);color:var(--pink);border-bottom:2px solid var(--pink)}
.gift{position:absolute;left:240px;top:716px;width:220px;height:180px;background:var(--pink);border-radius:8px;color:var(--white);display:flex;flex-direction:column;align-items:center;justify-content:center;gap:12px;font-weight:700;font-size:17px}
.campaign{position:absolute;left:480px;top:716px;width:460px;height:180px;background:var(--white);border-radius:8px;overflow:hidden}
.campaign-lead{position:absolute;left:36px;top:104px;font-size:20px;font-weight:800;color:var(--pink-deep)}
.campaign-lead b{font-size:30px}
.campaign-tag{position:absolute;left:36px;top:142px;background:var(--pink);color:var(--white);font-size:14px;font-weight:700;padding:4px 16px;border-radius:14px}

/* concierge */
.concierge-title{position:absolute;left:0;top:962px;width:1200px;text-align:center;font-size:24px;font-weight:800;color:var(--ink)}
.concierge-text{position:absolute;left:340px;top:1008px;width:520px;text-align:center;font-size:11px;line-height:1.9;color:var(--ink-light)}
.bubble{position:absolute;border-radius:50%;background:var(--white);border:2px solid var(--pink-soft);display:flex;align-items:center;justify-content:center;text-align:center;font-size:11px;line-height:1.7;color:var(--ink);padding:22px}

/* store */
.store{position:absolute;left:0;top:1372px;width:1200px;height:244px;background:var(--pink-pale)}
.store-badge{position:absolute;left:250px;top:1386px;width:80px;height:80px;border-radius:50%;background:var(--pink);color:var(--white);font-size:12px;font-weight:700;display:flex;align-items:center;justify-content:center;text-align:center;line-height:1.4}
.store-head{position:absolute;left:0;top:1392px;width:1200px;text-align:center}
.store-head span{display:inline-block;border-bottom:2px solid var(--pink);font-size:16px;font-weight:700;color:var(--pink-deep);padding:0 12px 2px}
.store-lead{position:absolute;left:0;top:1428px;width:1200px;text-align:center;font-size:26px;font-weight:800;color:var(--pink-deep)}
.store-row{position:absolute;left:300px;top:1476px;width:600px;display:flex;justify-content:space-between}
.store-item{width:92px;text-align:center;font-size:11px;color:var(--ink)}
.store-item .round{width:80px;height:80px;border-radius:50%;margin:0 auto 5px;background:linear-gradient(135deg,#f1ebe8,#d9dfe3);border:3px solid var(--white)}
.store-btn{position:absolute;left:520px;top:1584px;width:160px;height:24px;border-radius:12px;background:var(--white);border:1px solid var(--pink);color:var(--pink-deep);font-size:11px;display:flex;align-items:center;justify-content:center}

/* news */
.news-head{position:absolute;left:280px;top:1640px;width:440px;text-align:center;font-size:18px;font-weight:700;color:var(--ink)}
.news-list{position:absolute;left:280px;top:1676px;width:440px;list-style:none}
.news-list li{display:flex;align-items:center;gap:12px;height:28px;border-bottom:1px dotted #ddd;font-size:11px;color:var(--ink);white-space:nowrap}
.news-list time{width:70px;color:var(--ink-light)}
.tag{width:66px;flex:none;text-align:center;color:var(--white);font-size:10px;border-radius:3px;padding:2px 0;white-space:nowrap}
.tag.pink{background:var(--pink)}.tag.blue{background:var(--blue)}.tag.yellow{background:var(--yellow)}.tag.green{background:var(--green)}
.greeting-head{position:absolute;left:760px;top:1640px;width:170px;text-align:center;font-size:18px;font-weight:700}

/* footer */
.footer-ornament{position:absolute;left:470px;top:1900px;width:260px;height:130px;border-radius:65px;background:linear-gradient(180deg,var(--pink-soft),var(--pink))}
.footer-nav{position:absolute;left:240px;top:2070px;width:720px;display:flex}
.footer-nav a{flex:1;display:flex;flex-direction:column;align-items:center;gap:3px;font-size:10px;color:var(--ink);text-decoration:none;white-space:nowrap}
.footer-nav a svg{width:18px;height:18px}
.footer-bar{position:absolute;left:0;top:2146px;width:1200px;height:34px;background:var(--pink);color:var(--white);font-size:11px;display:flex;align-items:center;justify-content:center}
</style>
</head>
<body>
<div class="page">

  <header class="site-header">
    <div class="logo">〇〇眼鏡店</div>
    <div class="util-tabs"><span>店舗案内</span><span>採用情報</span><span>お問い合わせ</span></div>
    <nav class="global-nav">
      <a href="#"><svg viewBox="0 0 20 20"><path d="M3 10 L10 4 L17 10 V17 H3 Z" fill="none" stroke="#ef8a80" stroke-width="1.6"/></svg>ホーム</a>
      <a href="#"><svg viewBox="0 0 20 20"><circle cx="10" cy="10" r="7" fill="none" stroke="#ef8a80" stroke-width="1.6"/><path d="M10 6v5M10 13v1" stroke="#ef8a80" stroke-width="1.6"/></svg>はじめての方へ</a>
      <a href="#" class="active"><svg viewBox="0 0 20 20"><circle cx="6" cy="11" r="3.5" fill="none" stroke="#fff" stroke-width="1.6"/><circle cx="14" cy="11" r="3.5" fill="none" stroke="#fff" stroke-width="1.6"/><path d="M9.5 11h1" stroke="#fff" stroke-width="1.6"/></svg>メガネ</a>
      <a href="#"><svg viewBox="0 0 20 20"><ellipse cx="10" cy="11" rx="6" ry="4" fill="none" stroke="#ef8a80" stroke-width="1.6"/></svg>コンタクト</a>
      <a href="#"><svg viewBox="0 0 20 20"><rect x="4" y="6" width="12" height="10" fill="none" stroke="#ef8a80" stroke-width="1.6"/><path d="M3 6h14" stroke="#ef8a80" stroke-width="1.6"/></svg>お店について</a>
      <a href="#"><svg viewBox="0 0 20 20"><path d="M10 17s-5-5-5-9a5 5 0 0 1 10 0c0 4-5 9-5 9z" fill="none" stroke="#ef8a80" stroke-width="1.6"/><circle cx="10" cy="8" r="1.8" fill="#ef8a80"/></svg>店舗案内</a>
      <a href="#" style="border-right:none"><svg viewBox="0 0 20 20"><rect x="3" y="5" width="14" height="10" fill="none" stroke="#ef8a80" stroke-width="1.6"/><path d="M3 5l7 6 7-6" fill="none" stroke="#ef8a80" stroke-width="1.6"/></svg>お問い合わせ</a>
    </nav>
  </header>

  <section class="hero">
    <div class="photo side" style="left:0;top:0;width:250px;height:370px" role="img" aria-label="メガネをかけた子どもたちの写真"></div>
    <div class="photo" style="left:258px;top:0;width:684px;height:370px;background:linear-gradient(120deg,#e9dcd6,#d6dde3 60%,#e2d3cc)" role="img" aria-label="メガネをかけた学生の女の子の写真"></div>
    <div class="photo side" style="left:950px;top:0;width:250px;height:370px" role="img" aria-label="メガネ選びをする子どもの写真"></div>
    <div class="hero-copy">そのメガネ、お子様に<br>ちゃんと合ってますか？</div>
    <div class="hero-sub">成長期の目にぴったりの一本を、<br>専門スタッフが丁寧にお選びします。</div>
    <div class="hero-arrow" style="left:262px"><svg width="12" height="16" viewBox="0 0 12 16"><path d="M9 2L3 8l6 6" fill="none" stroke="#8f8784" stroke-width="2"/></svg></div>
    <div class="hero-arrow" style="left:908px"><svg width="12" height="16" viewBox="0 0 12 16"><path d="M3 2l6 6-6 6" fill="none" stroke="#8f8784" stroke-width="2"/></svg></div>
  </section>
  <div class="dots"><i class="on"></i><i></i><i></i></div>

  <section class="feature-band">
    <div class="photo" style="left:0;top:100px;width:228px;height:250px;opacity:.6" role="img" aria-label="店内の写真"></div>
    <div class="photo" style="left:952px;top:20px;width:248px;height:240px;opacity:.6" role="img" aria-label="メガネをかけた子どもたちの写真"></div>
  </section>

  <div class="card" style="left:240px;top:556px;width:220px;height:146px">
    <div class="card-title">めがねはこちら</div>
    <div class="photo" style="left:0;top:40px;width:220px;height:106px;background:linear-gradient(135deg,#fbf1ec,#f3d9c9)" role="img" aria-label="メガネフレームの写真"></div>
  </div>
  <div class="card" style="left:480px;top:556px;width:220px;height:146px">
    <div class="card-title alt">コンタクトはこちら</div>
    <div class="photo" style="left:0;top:42px;width:220px;height:104px;background:linear-gradient(135deg,#eef3f6,#d7e2ea)" role="img" aria-label="コンタクトレンズの写真"></div>
  </div>
  <div class="card" style="left:720px;top:556px;width:220px;height:146px">
    <div class="abs" style="right:12px;top:10px;font-size:12px;font-weight:700;color:var(--pink-deep);text-align:right;line-height:1.4">キッズメガネ<br>はこちら</div>
    <div class="photo" style="left:0;top:50px;width:220px;height:96px" role="img" aria-label="子ども用メガネの写真"></div>
  </div>

  <div class="gift">
    <svg width="54" height="54" viewBox="0 0 54 54"><rect x="8" y="22" width="38" height="26" fill="none" stroke="#fff" stroke-width="3"/><rect x="5" y="14" width="44" height="9" fill="none" stroke="#fff" stroke-width="3"/><path d="M27 14v34" stroke="#fff" stroke-width="3"/></svg>
    ギフトカード
  </div>
  <div class="campaign">
    <div class="photo" style="left:0;top:0;width:460px;height:96px;background:linear-gradient(90deg,#fbe4df,#f3efeb 50%,#dfe6ea)" role="img" aria-label="赤いメガネと子どもたちの写真"></div>
    <div class="campaign-lead">今ならなんと<b>20%</b>オフ!!</div>
    <div class="campaign-tag">ただいまキャンペーン中</div>
  </div>

  <section>
    <h2 class="concierge-title">〇〇眼鏡店はめがね選びのコンシェルジュです。</h2>
    <p class="concierge-text">地域のみなさまの目の健康を考え、一人ひとりに合ったメガネとコンタクトをご提案しています。<br>視力測定からフレーム選び、アフターケアまで、専門スタッフが丁寧にお手伝いいたします。<br>お気軽にご相談ください。</p>
    <div class="bubble" style="left:250px;top:1110px;width:160px;height:160px">似合うフレームを<br>一緒に探しますので<br>安心してご来店<br>ください。</div>
    <div class="bubble" style="left:790px;top:1080px;width:160px;height:160px">目のことなら<br>隣の眼科と連携して<br>しっかりサポート<br>いたします。</div>
    <div class="photo" style="left:440px;top:1110px;width:320px;height:244px;background:linear-gradient(180deg,#f6efea,#e8dcd4)" role="img" aria-label="カウンターに立つ二人のコンシェルジュのイラスト"></div>
  </section>

  <section class="store"></section>
  <div class="store-badge">ここが<br>安心</div>
  <div class="store-head"><span>店舗のご案内</span></div>
  <div class="store-lead">当店舗の隣には、眼科医院がございます。</div>
  <div class="store-row">
    <div class="store-item"><div class="round" role="img" aria-label="店舗外観の写真"></div>外観</div>
    <div class="store-item"><div class="round" role="img" aria-label="店内売り場の写真"></div>売り場</div>
    <div class="store-item"><div class="round" role="img" aria-label="視力測定室の写真"></div>測定室</div>
    <div class="store-item"><div class="round" role="img" aria-label="キッズコーナーの写真"></div>キッズ</div>
    <div class="store-item"><div class="round" role="img" aria-label="隣の眼科医院の写真"></div>眼科</div>
  </div>
  <div class="store-btn">→ 店舗案内はこちら</div>

  <section>
    <h2 class="news-head">新着情報</h2>
    <ul class="news-list">
      <li><time>2016.06.10</time><span class="tag pink">お知らせ</span>夏季休業日のご案内</li>
      <li><time>2016.06.05</time><span class="tag blue">メガネ</span>新作フレームが入荷しました</li>
      <li><time>2016.05.28</time><span class="tag yellow">キャンペーン</span>キッズメガネ20%オフ開催中</li>
      <li><time>2016.05.20</time><span class="tag green">コンタクト</span>新しいレンズの取扱い開始</li>
      <li><time>2016.05.12</time><span class="tag pink">お知らせ</span>ホームページを公開しました</li>
      <li><time>2016.05.01</time><span class="tag blue">メガネ</span>フィッティング無料実施中</li>
    </ul>
    <h2 class="greeting-head">代表挨拶</h2>
    <div class="photo" style="left:760px;top:1676px;width:170px;height:168px" role="img" aria-label="代表者の写真"></div>
  </section>

  <footer>
    <div class="footer-ornament" role="img" aria-label="ピンクのメガネ形の装飾"></div>
    <nav class="footer-nav">
      <a href="#"><svg viewBox="0 0 20 20"><path d="M3 10 L10 4 L17 10 V17 H3 Z" fill="none" stroke="#ef8a80" stroke-width="1.6"/></svg>ホーム</a>
      <a href="#"><svg viewBox="0 0 20 20"><circle cx="10" cy="10" r="7" fill="none" stroke="#ef8a80" stroke-width="1.6"/></svg>はじめての方へ</a>
      <a href="#"><svg viewBox="0 0 20 20"><circle cx="6" cy="11" r="3.5" fill="none" stroke="#ef8a80" stroke-width="1.6"/><circle cx="14" cy="11" r="3.5" fill="none" stroke="#ef8a80" stroke-width="1.6"/></svg>メガネ</a>
      <a href="#"><svg viewBox="0 0 20 20"><ellipse cx="10" cy="11" rx="6" ry="4" fill="none" stroke="#ef8a80" stroke-width="1.6"/></svg>コンタクト</a>
      <a href="#"><svg viewBox="0 0 20 20"><rect x="4" y="6" width="12" height="10" fill="none" stroke="#ef8a80" stroke-width="1.6"/></svg>お店について</a>
      <a href="#"><svg viewBox="0 0 20 20"><path d="M10 17s-5-5-5-9a5 5 0 0 1 10 0c0 4-5 9-5 9z" fill="none" stroke="#ef8a80" stroke-width="1.6"/></svg>店舗案内</a>
      <a href="#"><svg viewBox="0 0 20 20"><rect x="3" y="5" width="14" height="10" fill="none" stroke="#ef8a80" stroke-width="1.6"/><path d="M3 5l7 6 7-6" fill="none" stroke="#ef8a80" stroke-width="1.6"/></svg>お問い合わせ</a>
    </nav>
    <div class="footer-bar">© 〇〇眼鏡店 All Rights Reserved.</div>
  </footer>

</div>
</body>
</html>
```